Wordpress website for voluntary transgender support online

We need a website as an information support for transgender people and their friends and families. We are a self funded voluntary support group reaching out to educate all in need.
Fairly basic site. Tabs for 3 of us to put bios, professional resources and contacts, news, general information, our contact info, entertainment.
Our logo is attached and we'd love the use of clouds and the colour lilac. We wish to look professional but approachable and personable.

Target Market(s)

Transgender people,mr heir families and friends and general public.

Industry/Entity Type

Group

Requirements
Must have
• Willow 4 logo.
• Tabs for: about us, contacts, news, bios x3, suggestions, professional resources, entertainment, personal resources, general information.
• We are hoping to set up in Wordpress so that we can then manage the page and update in the future.
• Coding will be required.
Nice to have
• Any suggestions.

```html
<!DOCTYPE html>
<html lang="en">
<head>
<meta charset="utf-8">
<title>Willow 4 Transgender Support</title>
<link rel="stylesheet" href="https://fonts.googleapis.com/css2?family=Open+Sans:wght@300;400;600;700;800&display=swap">
<style>
  :root {
    --purple: #5b2d82;
    --purple-soft: #8a5aa8;
    --pink: #f2a7c0;
    --pink-pale: #fbe3ea;
    --grey-text: #777;
    --dark-text: #333;
    --line: #e4e4e4;
    --meta-bg: #f3f3f3;
    --footer-bg: #000;
    --footer-link: #f2a7c0;
    --white: #fff;
  }
  * { box-sizing: border-box; margin: 0; padding: 0; }
  html, body { width: 720px; height: 1200px; overflow: hidden; }
  body { font-family: "Open Sans", Arial, sans-serif; background: var(--white); color: var(--dark-text); }

  .site-header { height: 125px; text-align: center; }
  .brand { padding-top: 24px; display: flex; justify-content: center; align-items: center; gap: 10px; height: 80px; }
  .brand-dot { width: 22px; height: 22px; border-radius: 50%; background: var(--purple); }
  .brand-name { font-size: 38px; font-weight: 400; color: var(--purple); letter-spacing: 1px; line-height: 1; }
  .main-nav { display: flex; justify-content: space-between; align-items: center; padding: 22px 30px 0; }
  .main-nav a { font-size: 8.6px; font-weight: 700; color: var(--purple); text-decoration: none; letter-spacing: .2px; }
  .search-icon { width: 11px; height: 11px; }

  .hero { position: relative; height: 335px; background: linear-gradient(135deg, #d9cbc6 0%, #f0e4df 35%, #e9c9c2 60%, #cfb7b3 100%); display: flex; align-items: center; justify-content: center; }
  .hero-title { color: var(--white); font-size: 40px; font-weight: 700; letter-spacing: 1px; }
  .slider-dots { position: absolute; bottom: 14px; left: 50%; transform: translateX(-50%); display: flex; gap: 5px; }
  .slider-dots span { width: 15px; height: 15px; background: var(--pink); }
  .slider-dots span.active { background: var(--purple); }

  .features { height: 370px; display: flex; justify-content: center; gap: 10px; padding-top: 40px; }
  .feature { width: 175px; text-align: center; }
  .feature-icon { height: 120px; display: flex; align-items: flex-end; justify-content: center; }
  .icon-placeholder { width: 42px; height: 105px; background: var(--pink); }
  .icon-placeholder.symbol { width: 92px; height: 112px; background: var(--purple); }
  .feature-title { margin-top: 20px; font-size: 9.5px; font-weight: 800; color: var(--dark-text); }
  .feature-sub { font-size: 6.5px; font-weight: 600; color: var(--dark-text); margin-top: 3px; }
  .feature-label { font-size: 6.5px; color: var(--grey-text); margin-top: 12px; }
  .feature-text { font-size: 6.5px; color: var(--grey-text); line-height: 1.55; margin-top: 10px; padding: 0 12px; }
  .feature-meta { margin-top: 14px; background: var(--meta-bg); font-size: 6.5px; color: var(--grey-text); padding: 5px 0; display: flex; justify-content: center; gap: 4px; align-items: center; }
  .meta-icon { width: 6px; height: 7px; background: var(--grey-text); }
  .feature-bar { height: 3px; background: var(--pink); }
  .feature-bar.purple { background: var(--purple); }

  .promo { height: 166px; background: var(--pink-pale); text-align: center; padding-top: 16px; }
  .promo-title { font-size: 27px; font-weight: 400; color: var(--purple); line-height: 1.2; }
  .promo-text { font-size: 15px; font-weight: 300; color: var(--purple-soft); margin: 6px auto 0; width: 500px; line-height: 1.35; }
  .promo-button { display: inline-block; margin-top: 12px; background: var(--purple); color: var(--white); font-size: 15px; font-weight: 600; padding: 7px 38px; text-decoration: none; }

  .site-footer { height: 204px; background: var(--footer-bg); position: relative; }
  .footer-columns { display: flex; padding: 28px 0 0 161px; }
  .footer-col { width: 110px; }
  .footer-col:nth-child(2) { width: 103px; }
  .footer-col:nth-child(3) { width: 108px; }
  .footer-col h4 { font-size: 7.5px; font-weight: 700; color: var(--white); margin-bottom: 5px; }
  .footer-col a { display: block; font-size: 9px; font-weight: 600; color: var(--footer-link); text-decoration: none; line-height: 1.65; }
  .copyright { position: absolute; bottom: 14px; width: 100%; text-align: center; font-size: 7.5px; color: var(--purple-soft); }
</style>
</head>
<body>
  <header class="site-header">
    <div class="brand">
      <span class="brand-dot"></span>
      <span class="brand-name">Willow 4</span>
    </div>
    <nav class="main-nav">
      <a href="#">ABOUT US</a>
      <a href="#">NEWS</a>
      <a href="#">BIOS</a>
      <a href="#">SUGGESTIONS</a>
      <a href="#">PROFESSIONAL RESOURCES</a>
      <a href="#">ENTERTAINMENT</a>
      <a href="#">PERSONAL RESOURCES</a>
      <a href="#">GENERAL INFORMATION</a>
      <a href="#">CONTACT US</a>
      <svg class="search-icon" viewBox="0 0 12 12"><circle cx="5" cy="5" r="3.8" fill="none" stroke="#5b2d82" stroke-width="1.6"/><line x1="7.8" y1="7.8" x2="11" y2="11" stroke="#5b2d82" stroke-width="1.8"/></svg>
    </nav>
  </header>

  <section class="hero" role="img" aria-label="Photograph of caring hands holding each other">
    <h1 class="hero-title">MAIN TITLE GOES HERE</h1>
    <div class="slider-dots">
      <span></span><span class="active"></span><span></span><span></span><span></span><span></span><span></span><span></span>
    </div>
  </section>

  <section class="features">
    <article class="feature">
      <div class="feature-icon"><div class="icon-placeholder" role="img" aria-label="Pink illustration of a standing figure"></div></div>
      <h3 class="feature-title">LOREM IPSUM DOLOR</h3>
      <p class="feature-sub">Ei purto nec numero erat, sed dicta reprehendunt</p>
      <p class="feature-label">Nemo sensibus</p>
      <p class="feature-text">Duo fugit dilecta in, vis quas postea nostrud ut. Nec graeci signiferumque cu, eam latine tritani at, mollis vocent gloriatur te sed.</p>
      <div class="feature-meta"><span class="meta-icon"></span>Vitae moderatius</div>
      <div class="feature-bar"></div>
    </article>
    <article class="feature">
      <div class="feature-icon"><div class="icon-placeholder symbol" role="img" aria-label="Purple illustration of a gender symbol"></div></div>
      <h3 class="feature-title">LOREM IPSUM DOLOR</h3>
      <p class="feature-sub">Ei purto nec numero erat, sed dicta reprehendunt</p>
      <p class="feature-label">Nemo sensibus</p>
      <p class="feature-text">Duo fugit dilecta in, vis quas postea nostrud ut. Nec graeci signiferumque cu, eam latine tritani at, mollis vocent gloriatur te sed.</p>
      <div class="feature-meta"><span class="meta-icon"></span>Vitae moderatius</div>
      <div class="feature-bar purple"></div>
    </article>
    <article class="feature">
      <div class="feature-icon"><div class="icon-placeholder" role="img" aria-label="Pink illustration of a standing figure"></div></div>
      <h3 class="feature-title">LOREM IPSUM DOLOR</h3>
      <p class="feature-sub">Ei purto nec numero erat, sed dicta reprehendunt</p>
      <p class="feature-label">Nemo sensibus</p>
      <p class="feature-text">Duo fugit dilecta in, vis quas postea nostrud ut. Nec graeci signiferumque cu, eam latine tritani at, mollis vocent gloriatur te sed.</p>
      <div class="feature-meta"><span class="meta-icon"></span>Vitae moderatius</div>
      <div class="feature-bar"></div>
    </article>
  </section>

  <section class="promo">
    <h2 class="promo-title">Ei nostrud adipisci scripserit</h2>
    <p class="promo-text">Nulla errem iudico est in, odio placerat pri ea, id eum esse senobus. Ex vis case summo menandri.</p>
    <a class="promo-button" href="#">Learn more</a>
  </section>

  <footer class="site-footer">
    <div class="footer-columns">
      <div class="footer-col"><h4>FUN STUFF</h4><a href="#">Gift Certificates</a><a href="#">Referrals</a><a href="#">Training Center</a></div>
      <div class="footer-col"><h4>SUPPORT</h4><a href="#">FAQ</a><a href="#">Feedback</a><a href="#">Contact</a><a href="#">How it Works</a><a href="#">Testimonials</a></div>
      <div class="footer-col"><h4>COMPANY</h4><a href="#">About Us</a><a href="#">Partnership</a><a href="#">Blog</a></div>
      <div class="footer-col"><h4>FUN STUFF</h4><a href="#">Gift Certificates</a><a href="#">Referrals</a><a href="#">Training Center</a></div>
    </div>
    <p class="copyright">Copyright © Willow 4 Transgender Support</p>
  </footer>
</body>
</html>
```